Natural Handmade Cosmetics Line

I'm looking for a range of labels for a natural handmade Cosmetics company in UK. I'm looking to print the labels on a transparent substrate. The ingredients & Details are on the website. Vorenta means Lovely or beloved in latin. The products are designed & manufactured by hand but I want to give the impression of a high end cosmetic brand.

I would like a tag line of some description like "Natural, Pure, Handmade" included

The name of the company is vorenta cosmetics (www.vorenta.co.uk) and I have the following products (All skin types)

1. Orange & Rose Toner - 150ml (Length: 14cm / hight 9.5cm)
2. Grapefruit Cleanser - 150g (Length 14cm / Hight 9.5cm)
3. Balancing Facial Oil - 30ml (Length 10.5cm / Hight 4.6cm)
4. Frankincense & Neroli Facial Oil - 30ml (Length 10.5cm / Hight 4.6cm)
5. Neroli Moisturizing Face Cream - 50g (Length 15cm / Hight 5cm)
6. Lavender & Neroli Hand Cream - 100g (Length 15cm / Hight 8cm)
7. Tangerine Lip Balm - 4g (Length 5.4cm / Hight 4.6cm) - Lip Balm Tube
8. Mandarin Treatment Balm 50g (Length16.4cm / Hight 3.1cm)
9. Lemon & Tangerine Body Butter - 100g (Length 29cm / Hight 2.5cm)
10. Ylang Ylang & Bergamot Body Butter - 100g (Length 29cm / Hight 2.5cm)

Ideally in the future I would like to get some boxes designed.

I like the following designs

https://www.kestrova.co.uk/face/range/product-family/daily-essentials/
http://www.tolvanhue.co.uk/shop-for-products/natural-skin-care/organic-moisturiser-products
http://www.quobaskincare.com/
http://www.lumiskincare.com/
http://www.brindlemoorwellness.co.uk/organic-natural-skincare/dry-sensitive/lumiskincare-daily-moisture-for-men.html
Updates

Dimensions altered

Target Market(s)

Targeting woman of 25+

Industry/Entity Type

Cosmetics

Requirements
Must have
• The correct symbols which are included

```html
<!DOCTYPE html>
<html lang="en">
<head>
<meta charset="utf-8">
<title>Vorenta — Label Range</title>
<link rel="stylesheet" href="https://fonts.googleapis.com/css2?family=Cabin+Condensed:wght@400;500&family=Raleway:wght@300&display=swap">
<style>
  :root {
    --canvas: #ffffff;
    --label-edge: #dcdcdc;
    --brand-grey: #7d7d7d;
    --tagline-grey: #a3a3a3;
    --note-grey: #6e6e6e;
    --toner-orange: #f0821e;
    --oil-blue: #1f5fa8;
    --oil-green: #168a3c;
    --cleanser-purple: #4b2e8a;
    --cream-teal: #0f8a86;
    --hand-pink: #e3256b;
  }
  * { margin: 0; padding: 0; box-sizing: border-box; }
  html, body { width: 1200px; height: 1012px; overflow: hidden; background: var(--canvas); }
  .sheet { position: relative; width: 1200px; height: 1012px; }

  .label {
    position: absolute;
    border: 1px solid var(--label-edge);
    background: var(--canvas);
  }
  .label > * {
    position: absolute;
    left: 50%;
    transform: translateX(-50%);
    white-space: nowrap;
    text-align: center;
  }
  .wordmark {
    font-family: "Raleway", sans-serif;
    font-weight: 300;
    color: var(--brand-grey);
    letter-spacing: -0.02em;
    line-height: 1;
  }
  .tagline {
    font-family: "Raleway", sans-serif;
    font-weight: 300;
    color: var(--tagline-grey);
    line-height: 1;
  }
  .product {
    font-family: "Cabin Condensed", sans-serif;
    font-weight: 500;
    line-height: 1.25;
  }
  .volume {
    font-family: "Raleway", sans-serif;
    font-weight: 300;
    line-height: 1;
  }
  .skin-note {
    font-family: "Raleway", sans-serif;
    font-weight: 300;
    color: var(--note-grey);
    line-height: 1;
  }

  .toner { color: var(--toner-orange); }
  .oil-balancing { color: var(--oil-blue); }
  .oil-neroli { color: var(--oil-green); }
  .cleanser { color: var(--cleanser-purple); }
  .face-cream { color: var(--cream-teal); }
  .hand-cream { color: var(--hand-pink); }
</style>
</head>
<body>
<main class="sheet">

  <section class="label" style="left:11px;top:22px;width:537px;height:364px;">
    <div class="wordmark" style="top:126px;font-size:62px;">Vorenta</div>
    <div class="tagline" style="top:206px;font-size:17px;">Natural Handmade skincare</div>
    <div class="product toner" style="top:268px;font-size:16px;">Orange &amp; Rose Toner</div>
    <div class="volume toner" style="top:290px;font-size:14px;">150mle</div>
  </section>

  <section class="label" style="left:579px;top:20px;width:403px;height:177px;">
    <div class="wordmark" style="top:72px;font-size:31px;">Vorenta</div>
    <div class="tagline" style="top:112px;font-size:9px;">Natural Handmade skincare</div>
    <div class="product oil-balancing" style="top:137px;font-size:8px;">Balancing Facial Oil</div>
    <div class="volume oil-balancing" style="top:149px;font-size:7px;">150mle</div>
  </section>

  <section class="label" style="left:581px;top:225px;width:403px;height:177px;">
    <div class="wordmark" style="top:71px;font-size:31px;">Vorenta</div>
    <div class="tagline" style="top:112px;font-size:9px;">Natural Handmade skincare</div>
    <div class="product oil-neroli" style="top:131px;font-size:8px;">Neroli &amp; Frankincense<br>Facial Oil</div>
    <div class="volume oil-neroli" style="top:153px;font-size:7px;">30mle</div>
  </section>

  <section class="label" style="left:3px;top:431px;width:537px;height:365px;">
    <div class="wordmark" style="top:128px;font-size:62px;">Vorenta</div>
    <div class="tagline" style="top:207px;font-size:17px;">Natural Handmade skincare</div>
    <div class="product cleanser" style="top:261px;font-size:16px;">Grapefruit Cleanser</div>
    <div class="volume cleanser" style="top:283px;font-size:14px;">150mle</div>
  </section>

  <section class="label" style="left:579px;top:440px;width:576px;height:192px;">
    <div class="wordmark" style="top:61px;font-size:34px;">Vorenta</div>
    <div class="tagline" style="top:105px;font-size:10px;">Natural Handmade skincare</div>
    <div class="product face-cream" style="top:124px;font-size:9px;">Neroli Moisture<br>Facial Cream</div>
    <div class="volume face-cream" style="top:165px;font-size:8px;">15mle</div>
  </section>

  <section class="label" style="left:580px;top:670px;width:575px;height:307px;">
    <div class="wordmark" style="top:108px;font-size:52px;">Vorenta</div>
    <div class="tagline" style="top:175px;font-size:14px;">Natural Handmade skincare</div>
    <div class="product hand-cream" style="top:204px;font-size:16px;">Lavender &amp; Neroli<br>Hand&nbsp; Cream</div>
    <div class="skin-note" style="top:248px;font-size:9px;">All Skin Tipes</div>
    <div class="volume hand-cream" style="top:268px;font-size:12px;">160mle</div>
  </section>

</main>
</body>
</html>
```